Halvercott Orthodontics business card

Using our existing logo (created with ArtFolio), please create a tasteful, contemporary business card. We are father and daughter orthodontists specializing in braces, clarafit, etc to design healthy, beautiful smiles for children, adolescents, and adults. We would like the design to be family-friendly but not childish.
The final design should include all of the information without looking cluttered (I hope! If necessary to achieve an optimal design, please consider making the card double-sided)
Purple, black, silver on a white card
Please include the following information:
Halvercott Orthodontics (logo)
Marguerite L. Halvercott, DMD
Douglas R. Halvercott, DMD

312 Bramblewood Street
North Andover, MA 01899
978.555.0142

847C Quarry Hollow Street
Methuen, MA 01898
978.555.0187

email frontdesk@halvercottortho.example
website www.halvercottortho.example

```html
<!DOCTYPE html>
<html lang="en">
<head>
<meta charset="utf-8">
<title>Halvercott Orthodontics – Business Card</title>
<link rel="stylesheet" href="https://fonts.googleapis.com/css2?family=Lato:wght@400;700&display=swap">
<style>
  :root {
    --purple: #662a8c;
    --grey-text: #6d6d6d;
    --silver: #ece6f0;
    --white: #ffffff;
    --backdrop: #d9d9d7;
  }
  * { box-sizing: border-box; margin: 0; padding: 0; }
  html, body { width: 1200px; height: 1056px; overflow: hidden; }
  body {
    background: var(--backdrop);
    font-family: "Lato", sans-serif;
    display: flex;
    flex-direction: column;
    align-items: center;
    justify-content: center;
    gap: 40px;
  }
  .card {
    position: relative;
    width: 840px;
    height: 480px;
    border-radius: 36px;
    box-shadow: 0 10px 24px rgba(0,0,0,0.18);
    overflow: hidden;
  }
  .card-front { background: var(--white); }
  .card-back {
    background: var(--purple);
    display: flex;
    align-items: center;
    justify-content: center;
  }

  .edge-band {
    position: absolute;
    top: 0; right: 0; bottom: 0;
    width: 64px;
    background: var(--purple);
  }

  .brand {
    display: flex;
    align-items: center;
    gap: 16px;
    color: var(--purple);
    font-weight: 700;
    white-space: nowrap;
  }
  .brand-dot {
    width: 24px; height: 24px; border-radius: 50%;
    background: currentColor;
    flex: none;
  }
  .card-front .brand {
    position: absolute;
    top: 62px; left: 190px;
    font-size: 40px;
  }
  .card-back .brand { color: var(--silver); font-size: 54px; }

  .divider {
    position: absolute;
    left: 0; right: 64px; top: 168px;
    height: 2px;
    background: var(--purple);
  }

  .doctors {
    position: absolute;
    left: 56px; top: 196px;
    width: 380px;
    list-style: none;
    border-bottom: 2px solid var(--purple);
    padding-bottom: 10px;
  }
  .doctor-name {
    color: var(--purple);
    font-weight: 700;
    font-size: 24px;
    line-height: 1.35;
    white-space: nowrap;
  }

  .contact-list {
    position: absolute;
    left: 56px; top: 316px;
    list-style: none;
    color: var(--grey-text);
    font-size: 19px;
    line-height: 1.6;
  }
  .contact-list li { display: flex; align-items: center; gap: 12px; white-space: nowrap; }
  .contact-list svg { width: 18px; height: 18px; flex: none; }

  .offices {
    position: absolute;
    left: 480px; top: 196px;
    display: flex;
    flex-direction: column;
    gap: 18px;
  }
  .office {
    font-style: normal;
    color: var(--grey-text);
    font-size: 19px;
    line-height: 1.35;
    white-space: nowrap;
  }
</style>
</head>
<body>
  <section class="card card-front">
    <div class="brand"><span class="brand-dot"></span>Halvercott Orthodontics</div>
    <div class="divider"></div>
    <div class="edge-band"></div>

    <ul class="doctors">
      <li class="doctor-name">Marguerite L. Halvercott, DMD</li>
      <li class="doctor-name">Douglas R. Halvercott, DMD</li>
    </ul>

    <ul class="contact-list">
      <li>
        <svg viewBox="0 0 20 20" aria-hidden="true"><rect x="2" y="5" width="16" height="11" fill="#662a8c"/><path d="M2 5l8 6 8-6" fill="none" stroke="#fff" stroke-width="1.5"/></svg>
        frontdesk@halvercottortho.example
      </li>
      <li>
        <svg viewBox="0 0 20 20" aria-hidden="true"><circle cx="10" cy="10" r="8" fill="#662a8c"/><path d="M2 10h16M10 2c-4 4-4 12 0 16M10 2c4 4 4 12 0 16" fill="none" stroke="#fff" stroke-width="1"/></svg>
        www.halvercottortho.example
      </li>
    </ul>

    <div class="offices">
      <address class="office">
        312 Bramblewood Street<br>
        North Andover, MA 01899<br>
        978.555.0142
      </address>
      <address class="office">
        847C Quarry Hollow Street<br>
        Methuen, MA 01898<br>
        978.555.0187
      </address>
    </div>
  </section>

  <section class="card card-back">
    <div class="brand"><span class="brand-dot"></span>Halvercott Orthodontics</div>
  </section>
</body>
</html>
```